Pitch book for the 2025 K7R Global Skycup event in Muncie, Indiana, USA

Title: Fueling the Future of Aeromodeling: Sponsor the 2025 K7R Global Skycup
1. Event Overview
What: The 2025 ORV K7R Global Skycup for Aerobatic Model Aircraft.
When: August 9–16, 2025.
Where: Institute for Scale Flightcraft (ISF) Headquarters, Muncie, Indiana.
Hosted by: Institute for Scale Flightcraft (ISF) in partnership with the Federated Guild for Remote Stunt Piloting (FGRSP).
Participants: Top pilots from across the globe, including juniors and female competitors.
2. Why Sponsor?
Shaping the Future Workforce: Inspire youth to explore careers in aerospace, aviation, and unmanned systems (drones, RPVs), bridging hobbies and high-tech industries like Corvane, Halbrook Teller, and more.
Brand Visibility: Engage with a global audience of enthusiasts, professionals, and media at a premier international event.
Community Impact: Support an event that promotes innovation, STEM education, and cultural exchange.
3. Key Features of the Event
Cutting-Edge Venue: Over 1,100 acres of flying space tailored for precision aerobatics.
Diverse Competitions: Featuring junior and female classifications alongside world-class competitors.
Global Audience: Media coverage, live streams, and on-site spectators.
4. Sponsorship Opportunities
Title Sponsor ($50,000):
Naming rights: "Your Brand Presents the 2025 K7R Global Skycup."
Logo placement on all event materials, website, and livestreams.
Prime exhibit space at the venue.
Gold Sponsor ($25,000):
Prominent branding on materials and media.
Speaking opportunity at the opening or closing ceremony.
Silver Sponsor ($10,000):
Recognition in event communications.
Inclusion in the sponsor wall at the venue.
Event Sponsor ($5,000):
Branding on specific activities (e.g., banquet, practice days).
Custom Sponsorships: Tailored to fit corporate goals, including STEM outreach and branded giveaways.
5. Audience Demographics
Competitors: Over 100 elite pilots from 40+ countries.
Spectators & Supporters: Thousands of attendees, ranging from hobbyists to industry professionals.
Media Reach: Coverage by international aeromodelling and aerospace outlets.
6. STEM and Industry Connections
Showcase pathways from aeromodelling to careers in aviation, engineering, and defense.
Collaborate with sponsors on outreach programs for local schools and universities.
7. Marketing Benefits
Digital: Inclusion in newsletters, website, and social media campaigns.
On-Site Branding: Banners, booths, and branded giveaways.
Networking: Access to high-value attendees and industry leaders.
8. Budget Breakdown
Goal: Raise $180,000 to support the championship.
Funding Allocation:
$70,000: Event logistics (venue, staff, equipment).
$50,000: Participant support (travel subsidies, junior competitor outreach).
$30,000: Marketing and media coverage.
$20,000: Amenities and hospitality.
9. Call to Action
Be Part of the Legacy: Join us in creating a memorable event that not only crowns world champions but also inspires future innovators.
Contact Information:
Name: [Your Name]
Email: [Your Email]
Phone: [Your Phone]
Website: [Event Website Link]

```html
<!DOCTYPE html>
<html lang="en">
<head>
<meta charset="utf-8">
<title>2025 K7R Global Skycup – Sponsorship Pitch Book</title>
<link rel="stylesheet" href="https://fonts.googleapis.com/css2?family=Montserrat:wght@300;600;700;800&family=Lato:wght@400;700&display=swap">
<style>
:root{
  --navy:#0e1f4a;
  --navy-deep:#0a1a40;
  --red:#d2143f;
  --white:#ffffff;
  --ink:#111111;
  --grey-bg:#8a8a8a;
  --card:#f3f3f5;
  --chart-blue:#3b6fc4;
  --grid:#8fb0e0;
}
*{box-sizing:border-box;margin:0;padding:0}
html,body{width:854px;height:1200px;overflow:hidden;background:var(--grey-bg)}
body{position:relative;font-family:'Lato',sans-serif;color:var(--ink)}
.slide{position:absolute;width:367px;height:259px;overflow:hidden}
.col-l{left:55px}.col-r{left:433px}
.row-1{top:55px}.row-2{top:331px}.row-3{top:616px}.row-4{top:902px}
.abs{position:absolute}
.head{font-family:'Montserrat',sans-serif;font-weight:700}
.photo{position:absolute}

/* 1 cover */
.cover{background:var(--navy)}
.cover .photo{left:0;top:0;width:367px;height:170px;background:linear-gradient(180deg,#8fa6bd 0%,#7d8c74 45%,#2a3a5e 75%,var(--navy) 100%)}
.cover-title{left:28px;top:78px;color:var(--white);font-family:'Montserrat',sans-serif;font-weight:800;font-size:19.5px;line-height:19.5px;letter-spacing:.4px}
.cover-sub{left:28px;top:141px;color:var(--white);font-family:'Montserrat',sans-serif;font-weight:300;font-size:10.5px;line-height:15px}
.cover-date{left:60px;top:177px;color:var(--white);font-family:'Montserrat',sans-serif;font-weight:700;font-size:10.5px;line-height:11px}
.cover-venue{left:166px;top:178px;color:var(--white);font-family:'Montserrat',sans-serif;font-weight:700;font-size:8px;line-height:11px}
.cover-pill{left:28px;top:208px;width:314px;height:14px;border-radius:7px;background:var(--white);font-size:7px;font-weight:700;text-align:center;line-height:14px}
.cover-band{left:0;top:227px;width:367px;height:27px;background:var(--red);color:var(--white);font-size:5.8px;line-height:8px;padding:5px 30px}
.brand-mark{display:flex;align-items:center;gap:6px;color:var(--white);font-family:'Montserrat',sans-serif;font-weight:800}
.brand-mark .dot{width:12px;height:12px;border-radius:50%;background:var(--red);flex:none}
.cover .brand-mark{left:228px;top:100px;width:120px;font-size:15px;line-height:16px;background:var(--red);padding:14px 10px;border-radius:6px}
.cover .brand-mark .dot{background:var(--white)}

/* 2 why */
.why{background:var(--white)}
.why .photo{left:170px;top:0;width:197px;height:259px;background:linear-gradient(90deg,#ffffff 0%,#e9ecef 30%,#b7b9b4 60%,#a8947a 100%)}
.why h2{left:26px;top:47px;font-size:15px;letter-spacing:.6px}
.why-list{left:26px;top:84px;width:200px;list-style:none}
.why-list li{position:relative;padding-left:20px;font-size:6.6px;line-height:8.3px;margin-bottom:11px}
.why-list b{display:block}
.why-list svg{position:absolute;left:0;top:1px}

/* 3 features */
.features{background:var(--white)}
.vert{left:18px;top:224px;transform:rotate(-90deg);transform-origin:0 0;white-space:nowrap}
.vert .big{font-family:'Montserrat',sans-serif;font-weight:800;font-size:22px;line-height:22px;color:var(--ink);display:block}
.vert .small{font-family:'Montserrat',sans-serif;font-weight:800;font-size:15px;line-height:16px;color:var(--red);display:block}
.feat{left:77px;width:135px;font-size:6.5px;line-height:7.8px}
.feat h3{font-family:'Montserrat',sans-serif;font-weight:600;font-size:11px;line-height:12px}
.features .p1{left:220px;top:28px;width:67px;height:59px;background:linear-gradient(160deg,#7aa7d8,#e2e0dc 60%,#b9a788)}
.features .p2{left:250px;top:72px;width:104px;height:95px;background:linear-gradient(180deg,#3f7fd0 0%,#86b3e6 45%,#a89b82 100%)}
.features .p3{left:212px;top:141px;width:93px;height:82px;background:linear-gradient(160deg,#c8c4b8,#6b6a6a 60%,#3d3a3a)}

/* 4 tiers */
.tiers{background:var(--navy-deep)}
.tiers h2{left:0;top:22px;width:367px;text-align:center;color:var(--white);font-size:15.5px;letter-spacing:.5px}
.tier{left:33px;width:306px;height:45px;background:var(--white);display:flex}
.tier-name{width:82px;background:var(--red);color:var(--white);font-family:'Montserrat',sans-serif;font-weight:700;font-size:10px;line-height:10px;text-align:center;display:flex;flex-direction:column;justify-content:center}
.tier-name small{font-size:6.3px;margin-top:3px;letter-spacing:.4px}
.tier ul{flex:1;padding:0 6px 0 16px;font-size:5.3px;line-height:8.4px;display:flex;flex-direction:column;justify-content:center}

/* 5 audience */
.audience{background:var(--navy)}
.audience .photo{left:0;top:0;width:367px;height:150px;background:linear-gradient(180deg,#2f6fc6 0%,#6fa1dc 40%,#5c5d66 72%,var(--navy) 100%)}
.audience h2{left:0;top:110px;width:367px;text-align:center;color:var(--white);font-size:15.5px;letter-spacing:.3px}
.demo-card{top:148px;width:103px;height:86px;background:var(--card);text-align:center;padding-top:34px}
.demo-card h3{font-family:'Montserrat',sans-serif;font-weight:600;font-size:10px;line-height:12px}
.demo-card p{font-size:6px;line-height:8.2px;margin-top:5px}
.demo-icon{top:132px;width:44px;height:44px;border-radius:50%;background:var(--red);display:flex;align-items:center;justify-content:center}

/* 6 stem */
.stem{background:var(--white)}
.stem-panel{left:0;top:0;width:162px;height:259px;background:var(--navy-deep)}
.stem h2{left:20px;top:26px;color:var(--white);font-size:12px;line-height:16px}
.stem-body{left:20px;top:67px;width:120px;color:var(--white);font-size:6.3px;line-height:8.3px}
.stem-body p{margin-bottom:8px}
.stem .photo{left:20px;top:139px;width:122px;height:108px;background:linear-gradient(180deg,#5b8fd6 0%,#a7c3e4 45%,#6f7e5e 70%,#9e9a86 100%)}
.chart{left:180px;top:21px;width:168px;height:109px;border:1px solid #ccd3dd;background:var(--white)}
.stem h3{left:183px;top:140px;font-size:12px}
.benefits{left:183px;top:162px;width:176px;list-style:none}
.benefits li{position:relative;padding-left:15px;font-size:6.2px;line-height:8px;margin-bottom:8px}
.benefits b{display:block;font-family:'Montserrat',sans-serif;font-weight:600;font-size:8.3px;line-height:9.5px}
.benefits svg{position:absolute;left:0;top:1px}

/* 7 budget */
.budget{background:var(--white)}
.budget .photo{left:214px;top:0;width:153px;height:259px;background:linear-gradient(180deg,#7fa6cf 0%,#c7ccd0 45%,#545a6e 65%,#a9a287 100%)}
.budget h2{left:26px;top:64px;font-size:15px}
.goal{left:26px;top:92px;width:180px;font-size:10px;line-height:11px}
.alloc{left:26px;top:127px;width:185px;list-style:none}
.alloc li{position:relative;padding-left:13px;font-size:7px;line-height:9px;margin-bottom:10px}
.alloc b{color:var(--red)}
.alloc svg{position:absolute;left:0;top:0}

/* 8 contact */
.contact{background:var(--navy)}
.contact .photo{left:0;top:0;width:367px;height:259px;background:linear-gradient(180deg,#2b3f6e 0%,#1d3163 50%,#142656 100%)}
.contact .brand-mark{left:128px;top:62px;width:112px;font-size:14px;line-height:16px;background:var(--red);padding:14px 10px;border-radius:6px}
.contact .brand-mark .dot{background:var(--white)}
.tagline{left:20px;top:160px;width:327px;text-align:center;color:var(--white);font-family:'Montserrat',sans-serif;font-weight:700;font-size:8.3px;line-height:11px}
.divider{left:134px;top:185px;width:100px;height:1px;background:var(--red)}
.touch{left:0;top:189px;width:367px;text-align:center;color:var(--white);font-family:'Montserrat',sans-serif;font-weight:600;font-size:9px}
.contact-row{left:0;top:211px;width:367px;display:flex;justify-content:space-evenly;color:var(--white);font-family:'Montserrat',sans-serif;font-weight:300;font-size:8.6px}
.website{left:0;top:240px;width:367px;text-align:center;color:var(--white);font-family:'Montserrat',sans-serif;font-weight:700;font-size:5.8px;letter-spacing:1.6px}
</style>
</head>
<body>

<!-- Cover -->
<section class="slide cover col-l row-1">
  <div class="photo" role="img" aria-label="Pilots standing on an airfield holding aerobatic model aircraft"></div>
  <div class="abs brand-mark"><span class="dot"></span>K7R Global Skycup</div>
  <h1 class="abs cover-title">FUELING THE<br>FUTURE OF<br>AEROMODELING</h1>
  <p class="abs cover-sub">SPONSOR THE<br>2025 K7R GLOBAL SKYCUP</p>
  <svg class="abs" style="left:32px;top:176px" width="20" height="20" viewBox="0 0 20 20" aria-hidden="true">
    <rect x="1" y="3" width="18" height="16" rx="2" fill="var(--red)"/>
    <rect x="5" y="0" width="2" height="5" fill="var(--red)"/><rect x="13" y="0" width="2" height="5" fill="var(--red)"/>
    <g fill="var(--navy)"><rect x="4" y="8" width="3" height="3"/><rect x="8.5" y="8" width="3" height="3"/><rect x="13" y="8" width="3" height="3"/><rect x="4" y="13" width="3" height="3"/><rect x="8.5" y="13" width="3" height="3"/><rect x="13" y="13" width="3" height="3"/></g>
  </svg>
  <p class="abs cover-date">August 9–16,<br>2025</p>
  <svg class="abs" style="left:146px;top:177px" width="14" height="19" viewBox="0 0 14 19" aria-hidden="true">
    <path d="M7 0C3 0 0 3 0 7c0 5 7 12 7 12s7-7 7-12c0-4-3-7-7-7z" fill="var(--red)"/><circle cx="7" cy="7" r="2.6" fill="var(--navy)"/>
  </svg>
  <p class="abs cover-venue">Institute for Scale Flightcraft (ISF)<br>Headquarters, Muncie, Indiana.</p>
  <p class="abs cover-pill">Participants: Top pilots from across the globe, including juniors and female competitors.</p>
  <p class="abs cover-band">Hosted by: Institute for Scale Flightcraft (ISF) in partnership with the Federated Guild for Remote Stunt Piloting (FGRSP).</p>
</section>

<!-- Why sponsor -->
<section class="slide why col-r row-1">
  <div class="photo" role="img" aria-label="Silver championship trophies on a table at the airfield"></div>
  <h2 class="abs head">WHY SPONSOR?</h2>
  <ul class="abs why-list">
    <li><svg width="13" height="8" viewBox="0 0 13 8" aria-hidden="true"><path d="M0 0l13 4-13 4 4-4z" fill="var(--red)"/></svg><b>Shaping the Future Workforce:</b>Inspire youth to explore careers in aerospace, aviation, and unmanned systems (drones, RPVs), bridging hobbies and high-tech industries like Corvane, Halbrook Teller and more.</li>
    <li><svg width="13" height="8" viewBox="0 0 13 8" aria-hidden="true"><path d="M0 0l13 4-13 4 4-4z" fill="var(--red)"/></svg><b>Brand Visibility:</b>Engage with a global audience of enthusiasts, professionals, and media at a premier international event.</li>
    <li><svg width="13" height="8" viewBox="0 0 13 8" aria-hidden="true"><path d="M0 0l13 4-13 4 4-4z" fill="var(--red)"/></svg><b>Community Impact:</b>Support an event that promotes innovation, STEM education, and cultural exchange.</li>
  </ul>
</section>

<!-- Key features -->
<section class="slide features col-l row-2">
  <div class="abs vert"><span class="big">KEY FEATURES</span><span class="small">OF THE EVENT</span></div>
  <div class="abs feat" style="top:69px"><h3>Cutting-Edge Venue:</h3><p>Over 1,100 acres of flying space tailored for precision aerobatics.</p></div>
  <div class="abs feat" style="top:114px"><h3>Diverse Competitions:</h3><p>Featuring junior and female classifications alongside world-class competitors.</p></div>
  <div class="abs feat" style="top:160px"><h3>Global Audience:</h3><p>Media coverage, live streams, and on-site spectators.</p></div>
  <div class="photo p2" role="img" aria-label="Row of national flags above a crowd at the flying field"></div>
  <div class="photo p1" role="img" aria-label="Competitors posing with a colourful model aircraft"></div>
  <div class="photo p3" role="img" aria-label="Guests seated at round tables during the banquet"></div>
</section>

<!-- Sponsorship tiers -->
<section class="slide tiers col-r row-2">
  <h2 class="abs head">SPONSORSHIP OPPORTUNITIES</h2>
  <div class="abs tier" style="top:49px">
    <div class="tier-name">TITLE<br>SPONSOR<small>($50,000)</small></div>
    <ul><li>Naming rights: "Your Brand Presents the 2025 K7R Global Skycup."</li><li>Logo placement on all event materials, website, and livestreams.</li><li>Prime exhibit space at the venue.</li></ul>
  </div>
  <div class="abs tier" style="top:100px">
    <div class="tier-name">GOLD<br>SPONSOR<small>($25,000)</small></div>
    <ul><li>Prominent branding on materials and media.</li><li>Speaking opportunity at the opening or closing ceremony.</li></ul>
  </div>
  <div class="abs tier" style="top:150px">
    <div class="tier-name">SILVER<br>SPONSOR<small>($10,000)</small></div>
    <ul><li>Recognition in event communications.</li><li>Inclusion in the sponsor wall at the venue.</li></ul>
  </div>
  <div class="abs tier" style="top:201px">
    <div class="tier-name">EVENT<br>SPONSOR<small>($5,000)</small></div>
    <ul><li>Branding on specific activities (e.g., banquet, practice days).</li><li>Custom Sponsorships: Tailored to fit corporate goals, including STEM outreach and branded giveaways.</li></ul>
  </div>
</section>

<!-- Audience -->
<section class="slide audience col-l row-3">
  <div class="photo" role="img" aria-label="International flags flying over competitors gathered at the field"></div>
  <h2 class="abs head">AUDIENCE DEMOGRAPHICS</h2>
  <div class="abs demo-card" style="left:15px"><h3>Competitors</h3><p>Over 100 elite pilots<br>from 40+ countries.</p></div>
  <div class="abs demo-card" style="left:131px;padding-top:28px"><h3>Spectators &amp;<br>Supporters:</h3><p style="margin-top:3px">Thousands of attendees,<br>ranging from hobbyists to<br>industry professionals.</p></div>
  <div class="abs demo-card" style="left:245px"><h3>Media Reach</h3><p>Coverage by international<br>aeromodelling<br>and aerospace outlets.</p></div>
  <div class="abs demo-icon" style="left:45px"><svg width="20" height="18" viewBox="0 0 20 18" aria-hidden="true" fill="#fff"><circle cx="4" cy="9" r="2"/><circle cx="10" cy="9" r="2"/><circle cx="16" cy="9" r="2"/><rect x="2" y="12" width="4" height="6"/><rect x="8" y="12" width="4" height="6"/><rect x="14" y="12" width="4" height="6"/><path d="M2 5l5-3 4 2 6-4" stroke="#fff" stroke-width="1.4" fill="none"/></svg></div>
  <div class="abs demo-icon" style="left:161px"><svg width="20" height="20" viewBox="0 0 20 20" aria-hidden="true" fill="#fff"><path d="M4 10l6-8 3 2-2 4h6l1 3-4 7H6z"/></svg></div>
  <div class="abs demo-icon" style="left:275px"><svg width="20" height="18" viewBox="0 0 20 18" aria-hidden="true" fill="#fff"><rect x="0" y="0" width="9" height="8" rx="1.5"/><rect x="11" y="0" width="9" height="3.5" rx="1"/><rect x="11" y="4.5" width="9" height="3.5" rx="1"/><rect x="0" y="10" width="9" height="8" rx="1.5"/><rect x="11" y="10" width="9" height="8" rx="1.5"/><path d="M14 12l4 2-4 2z" fill="var(--red)"/></svg></div>
</section>

<!-- STEM & marketing -->
<section class="slide stem col-r row-3">
  <div class="abs stem-panel"></div>
  <h2 class="abs head">STEM and Industry<br>Connections</h2>
  <div class="abs stem-body">
    <p>Showcase pathways from aeromodelling to careers in aviation, engineering, and defense.</p>
    <p>Collaborate with sponsors on outreach programs for local schools and universities.</p>
  </div>
  <div class="photo" role="img" aria-label="Pilots lined up with their aerobatic model aircraft"></div>
  <svg class="abs chart" viewBox="0 0 168 109" aria-label="Rising bar chart with upward trend arrow" role="img">
    <g stroke="var(--grid)" stroke-width=".7">
      <path d="M14 8v84M26 8v84M38 8v84M50 8v84M62 8v84M74 8v84M86 8v84M98 8v84M110 8v84M122 8v84M134 8v84M146 8v84M152 8v84"/>
      <path d="M14 8h138M14 20h138M14 32h138M14 44h138M14 56h138M14 68h138M14 80h138M14 92h138"/>
    </g>
    <g fill="var(--chart-blue)">
      <rect x="26" y="87" width="7" height="4"/><rect x="37" y="86" width="7" height="5"/><rect x="48" y="85" width="7" height="6"/><rect x="59" y="83" width="7" height="8"/><rect x="70" y="80" width="7" height="11"/><rect x="81" y="76" width="7" height="15"/><rect x="92" y="70" width="7" height="21"/><rect x="103" y="60" width="7" height="31"/><rect x="114" y="46" width="7" height="45"/><rect x="125" y="26" width="7" height="65"/>
    </g>
    <path d="M20 88C60 84 95 78 112 52 120 40 124 30 127 20" stroke="#e01010" stroke-width="2" fill="none"/>
    <path d="M122 22l7-10 2 12z" fill="#e01010"/>
  </svg>
  <h3 class="abs head">Marketing Benefits</h3>
  <ul class="abs benefits">
    <li><svg width="11" height="11" viewBox="0 0 11 11" aria-hidden="true"><circle cx="5.5" cy="5.5" r="4.5" fill="none" stroke="var(--red)" stroke-width="1.2"/><path d="M3 5.5l2 2 5-6" stroke="var(--red)" stroke-width="1.6" fill="none"/></svg><b>Digital:</b>Inclusion in newsletters, website, and social media campaigns.</li>
    <li><svg width="11" height="11" viewBox="0 0 11 11" aria-hidden="true"><circle cx="5.5" cy="5.5" r="4.5" fill="none" stroke="var(--red)" stroke-width="1.2"/><path d="M3 5.5l2 2 5-6" stroke="var(--red)" stroke-width="1.6" fill="none"/></svg><b>On-Site Branding:</b>Banners, booths, and branded giveaways.</li>
    <li><svg width="11" height="11" viewBox="0 0 11 11" aria-hidden="true"><circle cx="5.5" cy="5.5" r="4.5" fill="none" stroke="var(--red)" stroke-width="1.2"/><path d="M3 5.5l2 2 5-6" stroke="var(--red)" stroke-width="1.6" fill="none"/></svg><b>Networking:</b>Access to high-value attendees and industry leaders.</li>
  </ul>
</section>

<!-- Budget -->
<section class="slide budget col-l row-4">
  <div class="photo" role="img" aria-label="Winners on the podium beneath national flags"></div>
  <h2 class="abs head">Budget Breakdown</h2>
  <p class="abs goal">Goal: Raise $180,000 to support the championship.Funding Allocation:</p>
  <ul class="abs alloc">
    <li><svg width="10" height="10" viewBox="0 0 10 10" aria-hidden="true"><circle cx="5" cy="5" r="5" fill="var(--red)"/><path d="M2.6 5l1.7 1.7 3.2-3.4" stroke="#fff" stroke-width="1.3" fill="none"/></svg><b>$70,000:</b> Event logistics (venue, staff, equipment).</li>
    <li><svg width="10" height="10" viewBox="0 0 10 10" aria-hidden="true"><circle cx="5" cy="5" r="5" fill="var(--red)"/><path d="M2.6 5l1.7 1.7 3.2-3.4" stroke="#fff" stroke-width="1.3" fill="none"/></svg><b>$50,000:</b> Participant support (travel subsidies, junior competitor outreach).</li>
    <li><svg width="10" height="10" viewBox="0 0 10 10" aria-hidden="true"><circle cx="5" cy="5" r="5" fill="var(--red)"/><path d="M2.6 5l1.7 1.7 3.2-3.4" stroke="#fff" stroke-width="1.3" fill="none"/></svg><b>$30,000:</b> Marketing and media coverage.</li>
    <li><svg width="10" height="10" viewBox="0 0 10 10" aria-hidden="true"><circle cx="5" cy="5" r="5" fill="var(--red)"/><path d="M2.6 5l1.7 1.7 3.2-3.4" stroke="#fff" stroke-width="1.3" fill="none"/></svg><b>$20,000:</b> Amenities and hospitality.</li>
  </ul>
</section>

<!-- Contact -->
<section class="slide contact col-r row-4">
  <div class="photo" role="img" aria-label="Faint navy-toned view of pilots and banners at the event"></div>
  <div class="abs brand-mark"><span class="dot"></span>K7R Global Skycup</div>
  <p class="abs tagline">Be Part of the Legacy: Join us in creating a memorable event that not only crowns world champions but also inspires future innovators.</p>
  <div class="abs divider"></div>
  <p class="abs touch">Get In Touch</p>
  <div class="abs contact-row"><span>Name: [Your Name]</span><span>Email: [Your Email]</span><span>Phone: [Your Phone]</span></div>
  <p class="abs website">Website: [Event Website Link]</p>
</section>

</body>
</html>
```